International Wine events organiser seeks simple but stunning business card

I am a freelance events, marketing and PR provider specialised in the Wine industry. I help wineries and wine regions reach trade and consumers in foreign markets through events, help with the websites and communications, press trips and promotional activities. I am looking for a business card which is simple yet effective and is linked to events and communication.

I work mainly - but exclusively - with Italian wineries organising events for them in foreign market.s

I would like to use red in the logo as my present website (lunabrendor.com) used grey and red (although I will be changing the design at a later date).

Target Market(s)

Wine producers, promotional bodies in wine sector, companies looking to hire event organisers,

Industry/Entity Type

Marketing

Requirements
Must have
• My Name - Luna Brendor
My address
My phone
My website : www.lunabrendor.com
my Blog : pebbleandtwig.me

Should not have
• Butterflies, stars, flowers, anything not particularly linked to wine - would like to keep it simple, modern and eye-catching without being too cliche.

```html
<!DOCTYPE html>
<html lang="en">
<head>
<meta charset="utf-8">
<title>Luna Brendor – Business Card</title>
<link rel="stylesheet" href="https://fonts.googleapis.com/css2?family=Tinos:wght@400;700&family=Arimo&display=swap">
<style>
  :root {
    --backdrop: #1e1e1e;
    --card: #3a3331;
    --card-edge: #2f2927;
    --accent-red: #d8262c;
    --ink-light: #ece8e6;
    --rule: #8f8886;
    --serif: "Tinos", "Times New Roman", serif;
    --sans: "Arimo", Arial, sans-serif;
  }
  * { box-sizing: border-box; margin: 0; padding: 0; }
  html, body { width: 1200px; height: 900px; overflow: hidden; }
  body { background: var(--backdrop); position: relative; }

  .card {
    position: absolute;
    background: var(--card);
    border: 1px solid var(--card-edge);
    box-shadow: 0 12px 30px rgba(0,0,0,.45);
    color: var(--ink-light);
  }

  /* Name mark: plain sans text with one square */
  .name-mark {
    display: flex;
    align-items: center;
    gap: 12px;
    font-family: var(--sans);
    font-weight: 400;
    color: var(--accent-red);
    white-space: nowrap;
  }
  .name-mark__square {
    flex: none;
    background: var(--accent-red);
  }
  .tagline { font-family: var(--sans); color: var(--ink-light); }

  /* ---- Back side (portrait) ---- */
  .card--back {
    left: 110px; top: 152px;
    width: 340px; height: 595px;
    padding: 40px 30px 0 30px;
  }
  .back-brand { display: flex; flex-direction: column; align-items: flex-end; }
  .back-brand .name-mark { font-size: 32px; }
  .back-brand .name-mark__square { width: 14px; height: 14px; }
  .back-brand .tagline {
    font-size: 11.5px; line-height: 1.35;
    text-align: right; margin-top: 14px; padding-right: 2px;
  }

  .holder-name {
    font-family: var(--serif);
    font-weight: 700;
    font-size: 24px;
    text-align: right;
    margin-top: 56px;
    padding-right: 6px;
  }
  .divider { height: 1px; background: var(--rule); margin-left: 34px; }
  .divider--name { margin-top: 12px; }

  .contact-list {
    list-style: none;
    font-family: var(--serif);
    font-size: 15px;
    line-height: 1.75;
    margin: 22px 0 22px 46px;
  }
  .label, .highlight { color: var(--accent-red); }

  .address {
    font-family: var(--serif);
    font-style: normal;
    font-size: 15px;
    line-height: 1.6;
    margin: 22px 0 0 46px;
  }

  /* ---- Front side (landscape) ---- */
  .card--front {
    left: 490px; top: 278px;
    width: 600px; height: 343px;
  }
  .front-brand {
    position: absolute;
    left: 62px; top: 125px;
    width: 480px;
  }
  .front-brand .name-mark { font-size: 44px; }
  .front-brand .name-mark__square { width: 18px; height: 18px; }
  .front-brand .tagline { font-size: 18.5px; letter-spacing: 0.3px; margin-top: 18px; }
</style>
</head>
<body>

  <section class="card card--back" aria-label="Business card back">
    <div class="back-brand">
      <div class="name-mark"><span class="name-mark__square"></span>Luna Brendor</div>
      <p class="tagline">Communication &amp; Events<br>For The World Of Wine</p>
    </div>

    <h1 class="holder-name">Luna Brendor</h1>
    <div class="divider divider--name"></div>

    <ul class="contact-list">
      <li><span class="label">T.</span> +49 170 5283 614</li>
      <li><span class="label">E:</span> Luna@lunabrendor.com</li>
      <li>www.<span class="highlight">lunabrendor</span>.com</li>
      <li><span class="label">my blog:</span> pebbleandtwig.me</li>
    </ul>

    <div class="divider"></div>

    <address class="address">
      Lindenhofer Strasse, 14<br>81549 Munich
    </address>
  </section>

  <section class="card card--front" aria-label="Business card front">
    <div class="front-brand">
      <div class="name-mark"><span class="name-mark__square"></span>Luna Brendor</div>
      <p class="tagline">Communication &amp; Events For The World Of Wine</p>
    </div>
  </section>

</body>
</html>
```